Business Card - Tally Forge

Need Business Card design for company named Tally Forge. Software development focused mainly on Brindle Kelvox & Vuro Apps. I've attached our logo with both a black and white background. Please add trademark symbol to logo when using.

```html
<!DOCTYPE html>
<html lang="en">
<head>
<meta charset="utf-8">
<title>Tally Forge – Business Card</title>
<link rel="stylesheet" href="https://fonts.googleapis.com/css2?family=Ubuntu:wght@400;500;700&family=Oswald:wght@500&family=Montserrat:wght@400&display=swap">
<style>
  :root {
    --stage: #e8e3da;
    --card: #0d0d0d;
    --red: #d9232d;
    --orange: #f29a2e;
    --yellow: #f2c21d;
    --white: #ffffff;
    --muted: #e6e6e6;
  }
  * { margin: 0; padding: 0; box-sizing: border-box; }
  html, body {
    width: 1200px;
    height: 800px;
    overflow: hidden;
    background: var(--stage);
  }
  .stage {
    position: relative;
    width: 1200px;
    height: 800px;
  }
  .card {
    position: absolute;
    top: 90px;
    width: 420px;
    height: 620px;
  }
  .card--front { left: 160px; }
  .card--back  { left: 620px; }
  .card__shape {
    position: absolute;
    inset: 0;
    width: 420px;
    height: 620px;
  }

  /* Front: company name */
  .brand {
    position: absolute;
    left: 60px;
    top: 370px;
    display: flex;
    align-items: center;
    gap: 14px;
  }
  .brand__dot {
    width: 22px;
    height: 22px;
    border-radius: 50%;
    background: var(--orange);
  }
  .brand__name {
    font-family: "Ubuntu", sans-serif;
    font-weight: 500;
    font-size: 46px;
    letter-spacing: -0.5px;
    color: var(--white);
  }

  /* Back: name badge */
  .badge {
    position: absolute;
    left: 70px;
    top: 262px;
    width: 290px;
    height: 40px;
    background: var(--red);
    border-radius: 6px;
    display: flex;
    align-items: center;
  }
  .badge__icon {
    position: absolute;
    left: -6px;
    width: 46px;
    height: 46px;
  }
  .badge__name {
    margin-left: 54px;
    font-family: "Oswald", sans-serif;
    font-weight: 500;
    font-size: 27px;
    letter-spacing: 1.5px;
    color: var(--white);
  }
  .role {
    position: absolute;
    left: 150px;
    top: 308px;
    font-family: "Montserrat", sans-serif;
    font-size: 15px;
    color: var(--muted);
  }

  .contacts {
    position: absolute;
    left: 80px;
    top: 362px;
    list-style: none;
  }
  .contact {
    display: flex;
    align-items: flex-start;
    gap: 16px;
    margin-bottom: 24px;
  }
  .contact__icon {
    flex: none;
    width: 26px;
    height: 26px;
    margin-top: 4px;
  }
  .contact__text {
    font-family: "Montserrat", sans-serif;
    font-size: 16px;
    line-height: 19px;
    color: var(--white);
  }
</style>
</head>
<body>
<main class="stage">

  <!-- Front of card -->
  <section class="card card--front" aria-label="Card front">
    <svg class="card__shape" viewBox="0 0 420 620" aria-hidden="true">
      <defs>
        <clipPath id="front-clip">
          <path d="M44 0 H376 A24 24 0 0 1 400 24 V210 Q400 250 420 254 V580 Q420 620 380 620 H40 Q0 620 0 580 V254 Q20 250 20 210 V24 A24 24 0 0 1 44 0 Z"/>
        </clipPath>
        <linearGradient id="front-fade" x1="0" y1="0" x2="0" y2="1">
          <stop offset="0" stop-color="#0d0d0d"/>
          <stop offset="0.35" stop-color="#e8892a"/>
          <stop offset="0.65" stop-color="#f2a02c"/>
          <stop offset="1" stop-color="#f2c21d"/>
        </linearGradient>
      </defs>
      <g clip-path="url(#front-clip)">
        <rect width="420" height="620" fill="var(--card)"/>
        <rect x="368" y="0" width="28" height="180" fill="var(--red)"/>
        <path d="M368 170 H396 V250 Q396 290 382 290 Q368 290 368 250 Z" fill="var(--red)"/>
        <rect x="368" y="290" width="28" height="330" fill="url(#front-fade)"/>
        <path d="M368 360 H396 V440 Q396 478 382 478 Q368 478 368 440 Z" fill="var(--orange)"/>
      </g>
      <circle cx="190" cy="92" r="32" fill="var(--stage)"/>
    </svg>
    <div class="brand">
      <span class="brand__dot"></span>
      <span class="brand__name">Tally Forge</span>
    </div>
  </section>

  <!-- Back of card -->
  <section class="card card--back" aria-label="Card back">
    <svg class="card__shape" viewBox="0 0 420 620" aria-hidden="true">
      <defs>
        <clipPath id="back-clip">
          <path d="M44 0 H376 A24 24 0 0 1 400 24 V210 Q400 250 420 254 V580 Q420 620 380 620 H40 Q0 620 0 580 V254 Q20 250 20 210 V24 A24 24 0 0 1 44 0 Z"/>
        </clipPath>
        <linearGradient id="back-fade" x1="0" y1="0" x2="0" y2="1">
          <stop offset="0" stop-color="#0d0d0d"/>
          <stop offset="0.35" stop-color="#e8892a"/>
          <stop offset="0.65" stop-color="#f2a02c"/>
          <stop offset="1" stop-color="#f2c21d"/>
        </linearGradient>
      </defs>
      <g clip-path="url(#back-clip)">
        <rect width="420" height="620" fill="var(--card)"/>
        <g transform="translate(420 0) scale(-1 1)">
          <rect x="368" y="0" width="28" height="180" fill="var(--red)"/>
          <path d="M368 170 H396 V250 Q396 290 382 290 Q368 290 368 250 Z" fill="var(--red)"/>
          <rect x="368" y="290" width="28" height="330" fill="url(#back-fade)"/>
          <path d="M368 360 H396 V440 Q396 478 382 478 Q368 478 368 440 Z" fill="var(--orange)"/>
        </g>
      </g>
      <circle cx="250" cy="92" r="32" fill="var(--stage)"/>
    </svg>

    <div class="badge">
      <svg class="badge__icon" viewBox="0 0 46 46" aria-hidden="true">
        <circle cx="23" cy="23" r="21" fill="var(--red)" stroke="var(--white)" stroke-width="4"/>
        <circle cx="23" cy="18" r="6" fill="var(--white)"/>
        <path d="M12 33 Q12 25 23 25 Q34 25 34 33 Z" fill="var(--white)"/>
      </svg>
      <span class="badge__name">ROWAN HALE</span>
    </div>
    <p class="role">Funding Owner</p>

    <ul class="contacts">
      <li class="contact">
        <svg class="contact__icon" viewBox="0 0 26 26" aria-hidden="true">
          <circle cx="13" cy="13" r="13" fill="var(--red)"/>
          <path d="M13 6 A5 5 0 0 1 18 11 Q18 14 13 20 Q8 14 8 11 A5 5 0 0 1 13 6 Z" fill="var(--card)"/>
          <circle cx="13" cy="11" r="2" fill="var(--red)"/>
        </svg>
        <span class="contact__text">Unit 7, 22 Harbour Lane<br>Westmere WA 6021</span>
      </li>
      <li class="contact">
        <svg class="contact__icon" viewBox="0 0 26 26" aria-hidden="true">
          <circle cx="13" cy="13" r="13" fill="var(--orange)"/>
          <rect x="8" y="7" width="10" height="12" rx="1.5" fill="var(--card)"/>
          <rect x="10" y="9" width="6" height="3" fill="var(--orange)"/>
        </svg>
        <span class="contact__text">P: (00) 5550.12345<br>F: (00) 5550.12345</span>
      </li>
      <li class="contact">
        <svg class="contact__icon" viewBox="0 0 26 26" aria-hidden="true">
          <circle cx="13" cy="13" r="13" fill="var(--yellow)"/>
          <circle cx="13" cy="13" r="7" fill="none" stroke="var(--card)" stroke-width="1.8"/>
          <ellipse cx="13" cy="13" rx="3" ry="7" fill="none" stroke="var(--card)" stroke-width="1.5"/>
          <line x1="6" y1="13" x2="20" y2="13" stroke="var(--card)" stroke-width="1.5"/>
        </svg>
        <span class="contact__text">rhale@tallyforge.net<br>www.tallyforge.net</span>
      </li>
    </ul>
  </section>

</main>
</body>
</html>
```